■依頼の目的/概要
当方販促で使用するメモ帳を販売しております。
年間と通じて企業様が挨拶に出向く時に使用するノベルティメモ帳の表紙のデザインをお願いします。

■依頼詳細
貰って嬉しいメモ帳の表紙を提案下さい。今扱っている実績デザインを添付いたします。

■重視するポイント
色使いなど制限はありませんが、貰ってうれしい配って嬉しいデザインを要望します。今扱っているメモ帳デザインの一部を添付いたしますが、全く新しいデザインを希望します。テンプレートを添付しておりますのでご利用下さい。また、いい提案がありましたら複数個採用いたします。

その他何かご不明な点がございましたら、お気軽にご質問下さい。
よろしくお願いいたします。
ランサーの皆様、今回たくさんのご提案ありがとうございました。来週中には複数個の採用予定しております。選定までもうしばらくお待ち下さいませ。

社内アンケートを行って決定しました。一息つけるデザインと若者受けする和風なデザインが選ばれたように思います。

今回の依頼でたくさんのランサーの皆様のご提案ありがとうございます。せっかく時間を割いて提案して下さったにも関わらず選択されなかったランサー様には申し訳けなく思っております。近々またメモ帳の表紙デザインを現在依頼する予定もあります。よろしければご提案下さいませ。

```html
<!DOCTYPE html>
<html lang="en">
<head>
<meta charset="utf-8">
<title>memo – notepad cover</title>
<link rel="stylesheet" href="https://fonts.googleapis.com/css2?family=Quicksand:wght@300;400&display=swap">
<style>
  :root {
    --paper: #ffffff;
    --cover: #3f3533;
    --cover-lift: #5a4f4c;
    --trim: #1a1a1a;
    --ink-light: #efeae8;
    --ink-soft: #bfb7b4;
    --mark: #555555;
  }
  html, body {
    margin: 0;
    padding: 0;
    width: 1200px;
    height: 3068px;
    overflow: hidden;
    background: var(--paper);
  }
  .sheet {
    position: relative;
    width: 1200px;
    height: 3068px;
    font-family: "Quicksand", sans-serif;
  }
  .artwork {
    position: absolute;
    inset: 0;
  }
  .title {
    position: absolute;
    left: 426px;
    top: 1812px;
    margin: 0;
    font-weight: 300;
    font-size: 226px;
    line-height: 170px;
    letter-spacing: 32px;
    color: var(--ink-light);
  }
  .features {
    position: absolute;
    left: 432px;
    top: 2190px;
    width: 340px;
    color: var(--ink-soft);
    font-weight: 300;
    font-size: 25px;
    letter-spacing: 2px;
  }
  .features p { margin: 0 0 36px; line-height: 28px; }
  .features .calendar-head {
    margin-bottom: 18px;
    padding-bottom: 8px;
    border-bottom: 2px solid var(--ink-soft);
  }
  .era-table {
    border-collapse: collapse;
    font-size: 25px;
    letter-spacing: 2px;
  }
  .era-table td { padding: 0 0 16px; line-height: 28px; }
  .era-table .year { width: 110px; }
  .angle-label {
    position: absolute;
    left: 690px;
    top: 2880px;
    font-size: 28px;
    font-weight: 300;
    color: var(--ink-soft);
  }
</style>
</head>
<body>
<div class="sheet">
  <svg class="artwork" width="1200" height="3068" viewBox="0 0 1200 3068" xmlns="http://www.w3.org/2000/svg">
    <defs>
      <linearGradient id="scale-fade" x1="0" y1="0" x2="1" y2="0">
        <stop offset="0" stop-color="var(--cover-lift)"/>
        <stop offset="1" stop-color="var(--cover)"/>
      </linearGradient>
      <radialGradient id="angle-fade" cx="0" cy="1" r="1.1">
        <stop offset="0" stop-color="var(--cover-lift)"/>
        <stop offset="1" stop-color="var(--cover)"/>
      </radialGradient>
    </defs>
    <g class="crop-marks" stroke="var(--mark)" stroke-width="2" fill="none">
      <path d="M120 0V80M0 120H80M1080 0V80M1120 120H1200"/>
      <path d="M600 0V90M480 60H720"/>
      <path d="M0 1532H120M40 1420V1640M1080 1532H1200M1160 1420V1640"/>
      <path d="M120 2988V3068M0 2952H80M1080 2988V3068M1120 2952H1200"/>
      <path d="M600 2980V3068M480 3010H720"/>
    </g>
    <rect class="panel-back" x="120" y="120" width="960" height="1388" fill="var(--cover)" stroke="var(--trim)" stroke-width="3"/>
    <rect class="panel-front" x="120" y="1560" width="960" height="1392" fill="var(--cover)" stroke="var(--trim)" stroke-width="3"/>
    <rect class="ruler-area" role="img" aria-label="Ruler scale along the left edge of the cover"
          x="122" y="1640" width="110" height="1270" fill="url(#scale-fade)"/>
    <rect class="protractor-area" role="img" aria-label="Protractor fan of lines in 5 degree steps"
          x="750" y="2320" width="328" height="630" fill="url(#angle-fade)"/>
  </svg>

  <h1 class="title">me<br>mo</h1>

  <div class="features">
    <p>scale</p>
    <p>protractor</p>
    <p class="calendar-head">AD-Japanese calendar</p>
    <table class="era-table">
      <tr><td class="year">2018</td><td>H30</td></tr>
      <tr><td class="year">2000</td><td>H12</td></tr>
      <tr><td class="year">1989</td><td>S64 / H1</td></tr>
      <tr><td class="year">1975</td><td>S50</td></tr>
      <tr><td class="year">1926</td><td>T15 / S1</td></tr>
      <tr><td class="year">1912</td><td>M45 / T1</td></tr>
    </table>
  </div>

  <div class="angle-label">5°</div>
</div>
</body>
</html>
```